Elegant Business Cards & Letterhead

We will need the following that need to be designed: Letterhead and Business Cards, there winer will be re-hired for the balance of our stationary needs. Text for the cards and letterheads:

- Corporate Card instead of name
- landline: +971 (4) 362 7041
- mobile: +971 56 2819 605
- 800TUTOR
- email: dubai@velmora-lune.com
- www.velmora-lune.com
- PO Box 387261
Address: Castellan Heights Suite 1708, Dubai UAE

Thank you

Target Market(s)

VIPs, HNWI, High-end Families.

Industry/Entity Type

Luxury Market

Font styles to use
Other font styles liked:
• as explained

Colors

Designer to choose only greyscale colors for use in the design.

Requirements
Must have
• Elegant, Simple, Luxurious, Minimalistic
Nice to have
• Luxury, Golds, Engravings,
Should not have
• Much colors, funky,

```html
<!DOCTYPE html>
<html lang="en">
<head>
<meta charset="utf-8">
<title>Velmora Lune – Business Cards</title>
<link rel="stylesheet" href="https://fonts.googleapis.com/css2?family=Marcellus&family=Arimo:wght@400&display=swap">
<style>
  :root {
    --bg: #d6d6d6;
    --paper: #ffffff;
    --ink: #0b0b0b;
    --muted: #3a3a3a;
    --card-w: 540px;
    --card-h: 309px;
    --radius: 22px;
  }
  * { box-sizing: border-box; margin: 0; padding: 0; }
  html, body { width: 1200px; height: 768px; overflow: hidden; }
  body {
    background: var(--bg);
    display: flex;
    align-items: center;
    justify-content: center;
    gap: 50px;
  }
  .card {
    position: relative;
    width: var(--card-w);
    height: var(--card-h);
    border-radius: var(--radius);
    overflow: hidden;
    box-shadow: 0 6px 18px rgba(0,0,0,0.18);
  }
  .brand {
    font-family: "Marcellus", serif;
    color: var(--ink);
    letter-spacing: 0.04em;
    white-space: nowrap;
  }
  /* front */
  .card--front { background: var(--paper); }
  .card--front .brand {
    position: absolute;
    left: 0; right: 0; top: 118px;
    text-align: center;
    font-size: 40px;
  }
  .card--front .web {
    position: absolute;
    left: 0; right: 0; bottom: 38px;
    text-align: center;
    font-family: "Arimo", sans-serif;
    font-size: 11px;
    letter-spacing: 0.32em;
    color: var(--muted);
  }
  /* back */
  .card--back { background: var(--ink); }
  .card--back .panel { position: absolute; inset: 0; }
  .card--back .brand {
    position: absolute;
    left: 292px; top: 150px;
    font-size: 26px;
  }
  .details {
    position: absolute;
    left: 36px; top: 34px;
    font-family: "Arimo", sans-serif;
    color: var(--paper);
    font-size: 13px;
    line-height: 16px;
  }
  .address { padding-left: 24px; margin-bottom: 24px; }
  .contacts { list-style: none; }
  .contacts li { display: flex; align-items: center; gap: 9px; }
  .contacts svg { width: 12px; height: 12px; flex: none; }
</style>
</head>
<body>

<section class="card card--front">
  <p class="brand">VELMORA LUNE</p>
  <p class="web">www.velmora-lune.com</p>
</section>

<section class="card card--back">
  <svg class="panel" viewBox="0 0 540 309" aria-hidden="true">
    <polyline points="352,0 226,158 322,309" fill="none" stroke="#ffffff" stroke-width="5"/>
    <polygon points="368,0 540,0 540,309 340,309 242,158" fill="#ffffff"/>
  </svg>

  <div class="details">
    <p class="address">PO Box 387261<br>Castellan Heights<br>Suite 1708, Dubai UAE</p>
    <ul class="contacts">
      <li>
        <svg viewBox="0 0 12 12"><path d="M3 1l2 2.5-1.2 1.3c.7 1.5 1.9 2.7 3.4 3.4L8.5 7 11 9l-1.2 2C5.5 11 1 6.5 1 2.2z" fill="#fff"/></svg>
        <span>+971 (4) 362 7041</span>
      </li>
      <li>
        <svg viewBox="0 0 12 12"><path d="M3 1l2 2.5-1.2 1.3c.7 1.5 1.9 2.7 3.4 3.4L8.5 7 11 9l-1.2 2C5.5 11 1 6.5 1 2.2z" fill="#fff"/></svg>
        <span>800TUTOR</span>
      </li>
      <li>
        <svg viewBox="0 0 12 12"><rect x="3" y="0.8" width="6" height="10.4" rx="1" fill="none" stroke="#fff" stroke-width="1.2"/><circle cx="6" cy="9.4" r=".7" fill="#fff"/></svg>
        <span>+971 56 2819 605</span>
      </li>
      <li>
        <svg viewBox="0 0 12 12"><rect x="0.8" y="2.4" width="10.4" height="7.2" fill="#fff"/><path d="M1 2.8l5 4 5-4" fill="none" stroke="#0b0b0b" stroke-width="1"/></svg>
        <span>dubai@velmora-lune.com</span>
      </li>
      <li>
        <svg viewBox="0 0 12 12"><circle cx="6" cy="6" r="5.2" fill="#fff"/><path d="M3 4c1.5 0 2 1 1.5 2S5 8.5 6 9M7.5 2.5c-.5 1 .5 1.5 1.5 1.5s1 1.5 .5 2.5" fill="none" stroke="#0b0b0b" stroke-width="1"/></svg>
        <span>www.velmora-lune.com</span>
      </li>
    </ul>
  </div>

  <p class="brand">VELMORA LUNE</p>
</section>

</body>
</html>
```